Velo Breeze 99% effectiveness against H1N1 and H5N1 viruses

Design a web landing page for Velo Breeze that will motivate consumers to click on the Buy Now button. We are going to drive traffic to the website and need to improve the existing landing page and motivate the customer. This is the current landing page https://quillstonecare.example/velo-breeze-system/. This product is an air filtration device that kills Covid-19 through the use of UV light. It also provides real time air quality monitoring.

Target Market(s)

direct to consumers and small business

Coding

Coded - Design and coding required

Number of Pages Required

1 page

Font styles to use
Sans Serif

Requirements
Must have
• A simple design with clean graphics. It shouldn't be overly wordy, it should show an image of the product and emphasizes that it kills Covid-19 as it filters the air. You can pull any of the text off of our existing landing page-the graphics need to be changed. https://quillstonecare.example/velo-breeze-system/
Nice to have
• This is a product that kills airborne Covid-19 making inside spaces much safer to live and work in. The emphasis should be on Covid-19.

```html
<!DOCTYPE html>
<html lang="en">
<head>
<meta charset="utf-8">
<title>Velo Breeze System – Quillstone Care</title>
<link href="https://fonts.googleapis.com/css2?family=Montserrat:wght@400;500;600;700&family=Open+Sans:ital,wght@0,400;0,600;1,400&display=swap" rel="stylesheet">
<style>
:root{
  --red:#a3160f;
  --red-deep:#7c0a05;
  --orange:#f8900b;
  --ink:#1d1d1d;
  --muted:#555;
  --blush:#f8ecec;
  --line:#e9dede;
}
*{box-sizing:border-box;margin:0;padding:0}
html,body{width:1200px;height:3960px;overflow:hidden}
body{position:relative;font-family:'Montserrat',sans-serif;color:var(--ink);background:#fff}
.abs{position:absolute}
.btn{position:absolute;display:flex;align-items:center;justify-content:center;gap:10px;border-radius:30px;font-family:'Montserrat',sans-serif;font-weight:700;font-size:15px;letter-spacing:.5px;text-transform:uppercase;color:#fff;background:var(--orange)}
.btn-outline{background:transparent;color:var(--red-deep);border:2px solid var(--red-deep)}
.play{width:32px;height:32px;border-radius:50%;background:#fff;display:flex;align-items:center;justify-content:center}
.underline{position:absolute;height:3px;width:52px;background:var(--red)}
.lorem{font-family:'Open Sans',sans-serif;color:var(--muted)}

/* hero */
.hero{position:absolute;left:0;top:0;width:1200px;height:722px;background:linear-gradient(180deg,#ececec 0%,#f5f5f5 55%,#e4e4e4 100%)}
.hero-scene{position:absolute;left:560px;top:0;width:640px;height:722px;background:radial-gradient(ellipse at 60% 55%,#dcdcdc 0%,#e9e9e9 50%,rgba(236,236,236,0) 80%)}
.brand{position:absolute;left:88px;top:34px;display:flex;align-items:center;gap:10px;font-weight:700;font-size:18px;color:var(--red-deep);letter-spacing:-.3px}
.brand i{width:28px;height:28px;background:var(--red);display:block}
.nav{position:absolute;top:40px;font-size:12.5px;font-weight:500;color:#333;letter-spacing:.3px}
.nav.active{font-weight:700;color:#111;font-size:14px;top:39px}
.contact-pill{position:absolute;left:928px;top:28px;width:120px;height:41px;border-radius:22px;background:#fff;font-size:11px;font-weight:700;color:var(--red-deep);display:flex;align-items:center;justify-content:center}
.cart{position:absolute;left:1071px;top:28px;width:40px;height:40px;border-radius:50%;background:var(--red);display:flex;align-items:center;justify-content:center}
.hero h1{position:absolute;left:112px;top:244px;font-size:56px;font-weight:400;letter-spacing:.5px;color:#111}
.hero h1 b{font-weight:700}
.hero .sub{position:absolute;left:112px;top:318px;font-size:29px;line-height:37px;font-weight:400;color:#222}
.dots{position:absolute;top:683px;left:556px;display:flex;gap:10px}
.dots span{width:28px;height:4px;background:#bdbdbd}
.dots span.on{background:var(--red)}

/* filter */
.filter-art{position:absolute;left:100px;top:776px;width:476px;height:468px;border-radius:50%;background:radial-gradient(circle,#bdbdbd 0%,#dcdcdc 45%,#f4f4f4 75%,#fff 100%)}
.filter h2{position:absolute;left:636px;top:830px;font-size:39px;line-height:45px;font-weight:400;color:#111}
.filter h2 b{font-weight:700}
.filter p{position:absolute;left:636px;width:470px;font-size:13.5px;line-height:23px}

/* why */
.why-band{position:absolute;left:0;top:1298px;width:1200px;height:742px;background:var(--blush)}
.why-title{position:absolute;left:0;width:1200px;top:1355px;text-align:center;font-size:34px;font-weight:500;color:#111}
.why-title b{color:var(--red);font-weight:700}
.feat{position:absolute;width:260px}
.feat h4{font-size:14.5px;font-weight:700;color:#111;margin-bottom:6px}
.feat p{font-family:'Open Sans',sans-serif;font-size:12.5px;line-height:19px;color:#444}
.feat.left{text-align:right}
.icon{position:absolute;width:104px;height:104px;margin:-52px 0 0 -52px;border-radius:50%;background:var(--red);border:5px solid #fff;box-shadow:0 0 0 2px var(--red);display:flex;align-items:center;justify-content:center}

/* buy */
.buy-photo{position:absolute;left:614px;top:2040px;width:586px;height:562px;background:linear-gradient(90deg,#fff 0%,#f1efec 25%,#e8ded6 60%,#d8e0cf 100%)}
.buy h2{position:absolute;left:108px;top:2140px;font-size:34px;line-height:44px;font-weight:400}
.buy h2 b{color:var(--red);font-weight:700}
.device{position:absolute;border-radius:28%;background:linear-gradient(90deg,#f6f6f6 0%,#e3e3e3 55%,#9b9b9b 100%)}

/* reviews */
.reviews h2{position:absolute;left:0;width:1200px;top:2652px;text-align:center;font-size:31px;font-weight:400}
.reviews h2 b{font-weight:700}
.card{position:absolute;background:#fff;box-shadow:0 3px 14px rgba(0,0,0,.12);text-align:center}
.stars{color:var(--orange);letter-spacing:2px}
.card p{font-family:'Open Sans',sans-serif;font-style:italic;color:#555;margin:0 auto}
.avatar{border-radius:50%;background:linear-gradient(135deg,#cfc1b5,#8e7b6d);margin:0 auto}
.card .name{color:var(--orange);font-weight:600;letter-spacing:.5px}
.card .loc{color:#555;font-weight:600;letter-spacing:.3px}

/* contact */
.contact h2{position:absolute;left:0;width:1200px;top:3262px;text-align:center;font-size:34px;font-weight:400;color:#fff}
.contact h2 b{font-weight:700}
.contact .lead{position:absolute;left:0;width:1200px;top:3316px;text-align:center;font-family:'Open Sans',sans-serif;font-size:15px;color:#f3d0cc}
.field{position:absolute;background:#fff;border-radius:16px;font-family:'Open Sans',sans-serif;font-size:14px;color:#8a8a8a;padding:0 26px;display:flex;align-items:center}

/* footer */
.foot-nav{position:absolute;top:3780px;font-size:15px;font-weight:700;color:#111;transform:translateX(-50%)}
.copy{position:absolute;left:0;width:1200px;top:3816px;text-align:center;font-size:12.5px;color:#333}
.social{position:absolute;top:3854px;width:36px;height:36px;border-radius:50%;background:#1f1f1f}
</style>
</head>
<body>

<!-- Header and hero -->
<section class="hero">
  <div class="hero-scene" role="img" aria-label="Bright living room with a wall-mounted air purifier, armchair, brass floor lamp and potted plants"></div>
  <div class="brand"><i></i>Quillstone Care</div>
  <span class="nav active" style="left:384px">HOME</span>
  <span class="nav" style="left:484px">ABOUT US</span>
  <span class="nav" style="left:602px">PRODUCTS</span>
  <span class="nav" style="left:728px">SERVICES</span>
  <span class="nav" style="left:843px">SHOP</span>
  <div class="contact-pill">CONTACT US</div>
  <div class="cart">
    <svg width="22" height="20" viewBox="0 0 22 20" fill="none" stroke="#fff" stroke-width="1.8"><path d="M1 2h3l3 11h11l2-8H6"/><circle cx="8" cy="17" r="1.5"/><circle cx="17" cy="17" r="1.5"/></svg>
  </div>
  <h1><b>Velo Breeze</b> System</h1>
  <p class="sub">The World’s Smartest Air<br>Management Platform</p>
  <div class="btn" style="left:106px;top:421px;width:177px;height:54px">Buy Now
    <svg width="10" height="14" viewBox="0 0 10 14" fill="none" stroke="#fff" stroke-width="2.4"><path d="M2 1l6 6-6 6"/></svg></div>
  <div class="btn btn-outline" style="left:298px;top:421px;width:176px;height:54px">Learn More</div>
  <div class="dots"><span></span><span></span><span class="on"></span></div>
</section>

<!-- Air filter -->
<section class="filter">
  <div class="filter-art" role="img" aria-label="Exploded view of the purifier's filter layers in front of a wireframe virus particle"></div>
  <h2>Our Air Filter<br><b>kills Airborne Covid-19</b></h2>
  <div class="underline" style="left:636px;top:928px"></div>
  <p class="lorem" style="top:960px">On March 15, 2020, I was hit with two pieces of news that I think many people are dealing with during this pandemic.</p>
  <p class="lorem" style="top:1020px">At breakfast, I was told that a friend was given last rites on a ventilator as a result of their battle with Corona virus, COVID-19.&nbsp; That same afternoon, I learned that a friend who was a hardworking, imaginative and crazy but altruistic business</p>
  <div class="btn" style="left:637px;top:1152px;width:156px;height:46px;font-size:13px">Learn More</div>
</section>

<!-- Why choose -->
<section class="why">
  <div class="why-band"></div>
  <svg class="abs" style="left:0;top:1298px" width="1200" height="742" viewBox="0 1298 1200 742">
    <circle cx="599" cy="1659" r="172" fill="none" stroke="#e6d4d4" stroke-width="1.5"/>
    <circle cx="599" cy="1659" r="130" fill="#fdf7f7"/>
    <path d="M370 1524 Q352 1595 352 1667 Q352 1740 369 1809" fill="none" stroke="#a3160f" stroke-width="2"/>
    <path d="M825 1524 Q845 1595 845 1667 Q845 1740 826 1809" fill="none" stroke="#a3160f" stroke-width="2"/>
  </svg>
  <div class="device" style="left:522px;top:1574px;width:168px;height:174px" role="img" aria-label="Velo Breeze purifier, front view"></div>
  <h2 class="why-title">Why Choose <b>Velo Breeze System</b></h2>
  <div class="underline" style="left:574px;top:1410px"></div>

  <div class="icon" style="left:370px;top:1524px"><svg width="40" height="44" viewBox="0 0 40 44" fill="#fff"><rect x="15" y="4" width="8" height="20" rx="2"/><rect x="8" y="36" width="26" height="4" rx="2"/><path d="M26 18a10 10 0 0 1-4 18h-6v-4h6a6 6 0 0 0 2-11z"/></svg></div>
  <div class="icon" style="left:352px;top:1667px"><svg width="30" height="40" viewBox="0 0 30 40" fill="#fff"><path d="M15 2C10 12 4 19 4 26a11 11 0 0 0 22 0C26 19 20 12 15 2z"/></svg></div>
  <div class="icon" style="left:369px;top:1809px"><svg width="44" height="44" viewBox="0 0 44 44" fill="#fff" stroke="#fff" stroke-width="3"><circle cx="22" cy="22" r="8"/><path d="M22 2v7M22 35v7M2 22h7M35 22h7M8 8l5 5M31 31l5 5M8 36l5-5M31 13l5-5"/></svg></div>
  <div class="icon" style="left:825px;top:1524px"><svg width="44" height="40" viewBox="0 0 44 40" fill="#fff"><rect x="8" y="4" width="9" height="24" rx="4"/><rect x="27" y="4" width="9" height="24" rx="4"/><rect x="4" y="32" width="36" height="5" rx="2"/></svg></div>
  <div class="icon" style="left:845px;top:1667px"><svg width="40" height="44" viewBox="0 0 40 44" fill="#fff"><circle cx="20" cy="13" r="9"/><path d="M4 42c0-10 7-16 16-16s16 6 16 16z"/></svg></div>
  <div class="icon" style="left:826px;top:1809px"><svg width="46" height="36" viewBox="0 0 46 36" fill="none" stroke="#fff" stroke-width="4" stroke-linecap="round"><path d="M4 12h26a6 6 0 1 0-6-6M4 22h32a6 6 0 1 1-6 6M10 17h20"/></svg></div>

  <div class="feat left" style="left:32px;top:1488px"><h4>COVID-19 PCR Test</h4><p>Lorem ipsum dolar sit amet, cons<br>ctetuer adipiscing alit.</p></div>
  <div class="feat left" style="left:24px;top:1635px"><h4>Rapid COVID-19 Antibody Test</h4><p>Lorem ipsum dolar sit amet, cons<br>ctetuer adipiscing alit.</p></div>
  <div class="feat left" style="left:36px;top:1789px"><h4>UV Sterlization Device</h4><p>Lorem ipsum dolar sit amet, cons<br>ctetuer adipiscing alit.</p></div>
  <div class="feat" style="left:892px;top:1488px"><h4>Swabs</h4><p>Lorem ipsum dolar sit amet, cons<br>ctetuer adipiscing alit.</p></div>
  <div class="feat" style="left:915px;top:1635px;width:285px"><h4>Acute Respiratory Disese Masks</h4><p>Lorem ipsum dolar sit amet, cons<br>ctetuer adipiscing alit.</p></div>
  <div class="feat" style="left:898px;top:1778px"><h4>VELO AIR FILTER</h4><p>Lorem ipsum dolar sit amet, cons<br>ctetuer adipiscing alit.</p></div>

  <div class="btn" style="left:470px;top:1905px;width:270px;height:53px;font-size:15px;padding-left:26px;justify-content:space-between;padding-right:12px">Buy Our Product
    <span class="play"><svg width="10" height="12" viewBox="0 0 10 12"><path d="M1 0l9 6-9 6z" fill="#f8900b"/></svg></span></div>
</section>

<!-- Buy now -->
<section class="buy">
  <div class="buy-photo" role="img" aria-label="Smiling family: a father carrying his daughter on his shoulders while the mother holds him"></div>
  <h2>Buy Now Our<br><b>Velo Breeze System</b></h2>
  <p class="lorem abs" style="left:108px;top:2250px;width:380px;font-size:13.5px;line-height:26px">Quillstone Care is excited to partner with Velo Breeze to provide consumers and businesses with The World’s Smartest Air Management Platform</p>
  <div class="abs" style="left:108px;top:2340px;font-size:28px;font-weight:700">$449.00</div>
  <div class="btn" style="left:98px;top:2398px;width:155px;height:46px;font-size:14px">Buy Now</div>
  <div class="device" style="left:392px;top:2345px;width:161px;height:169px;box-shadow:0 16px 26px rgba(0,0,0,.12)" role="img" aria-label="Velo Breeze purifier, angled view"></div>
</section>

<!-- Reviews -->
<section class="reviews">
  <h2>Check Out Our <b>Coustumer Reviews</b></h2>
  <div class="underline" style="left:574px;top:2697px"></div>
  <svg class="abs" style="left:76px;top:2868px" width="30" height="52" viewBox="0 0 30 52" fill="none" stroke="#b8b8b8" stroke-width="2"><path d="M28 2L4 26l24 24"/></svg>
  <svg class="abs" style="left:1106px;top:2868px" width="30" height="52" viewBox="0 0 30 52" fill="none" stroke="#b8b8b8" stroke-width="2"><path d="M2 2l24 24L2 50"/></svg>

  <div class="card" style="left:143px;top:2760px;width:276px;height:289px;padding-top:34px">
    <div class="stars" style="font-size:14px">★★★★☆</div>
    <p style="width:236px;font-size:11.5px;line-height:21px;font-style:normal;margin-top:8px">Lorem Ipsum is simply dummy text of the printing and typesetting industry. Lorem Ipsum has been the industry's standard dummy .</p>
    <div class="avatar" style="width:52px;height:52px;margin-top:14px" role="img" aria-label="Customer portrait"></div>
    <div class="name" style="font-size:12px;margin-top:12px">DANA REYES</div>
    <div class="loc" style="font-size:10px;margin-top:6px">NEW YORK,NY</div>
  </div>
  <div class="card" style="left:439px;top:2736px;width:341px;height:331px;padding-top:40px">
    <div class="stars" style="font-size:17px">★★★★☆</div>
    <p style="width:300px;font-size:14.5px;line-height:24px;margin-top:10px">Lorem Ipsum is simply dummy text of the printing and typesetting industry. Lorem Ipsum has been the industry's standard dummy .</p>
    <div class="avatar" style="width:64px;height:64px;margin-top:18px" role="img" aria-label="Customer portrait"></div>
    <div class="name" style="font-size:14px;margin-top:12px">DANA REYES</div>
    <div class="loc" style="font-size:10.5px;margin-top:6px">NEW YORK,NY</div>
  </div>
  <div class="card" style="left:797px;top:2760px;width:277px;height:289px;padding-top:34px">
    <div class="stars" style="font-size:14px">★★★★☆</div>
    <p style="width:236px;font-size:11.5px;line-height:21px;font-style:normal;margin-top:8px">Lorem Ipsum is simply dummy text of the printing and typesetting industry. Lorem Ipsum has been the industry's standard dummy .</p>
    <div class="avatar" style="width:52px;height:52px;margin-top:14px" role="img" aria-label="Customer portrait"></div>
    <div class="name" style="font-size:12px;margin-top:12px">DANA REYES</div>
    <div class="loc" style="font-size:10px;margin-top:6px">NEW YORK,NY</div>
  </div>

  <div class="btn" style="left:498px;top:3112px;width:224px;height:42px;font-size:16px;text-transform:none;padding-left:22px;padding-right:6px;justify-content:space-between">View All Reviews
    <span class="play" style="width:30px;height:30px"><svg width="10" height="12" viewBox="0 0 10 12"><path d="M1 0l9 6-9 6z" fill="#f8900b"/></svg></span></div>
</section>

<!-- Contact -->
<section class="contact">
  <svg class="abs" style="left:0;top:3214px" width="1200" height="540" viewBox="0 0 1200 540">
    <path d="M0 0H1200V318C900 490 420 560 0 360Z" fill="#7c0a05"/>
    <path d="M0 360C420 560 900 490 1200 318V336C900 520 420 580 0 392Z" fill="#f8900b"/>
  </svg>
  <h2>Contact <b>Us</b></h2>
  <p class="lead">Lorem ipsum dolor sit amet, consectetur adipiscing elit, sed do</p>
  <div class="field" style="left:221px;top:3367px;width:372px;height:46px">Name</div>
  <div class="field" style="left:221px;top:3428px;width:372px;height:46px">Email address</div>
  <div class="field" style="left:221px;top:3490px;width:372px;height:46px">Phone Number</div>
  <div class="field" style="left:602px;top:3367px;width:372px;height:169px;align-items:flex-start;padding-top:20px">Write your message</div>
  <div class="btn" style="left:505px;top:3560px;width:171px;height:53px;font-size:15px">Send Now</div>
</section>

<!-- Footer -->
<footer>
  <div class="abs" style="left:0;top:3754px;width:1200px;height:206px;background:linear-gradient(180deg,#fff 0%,#f1f1f1 100%);z-index:-1"></div>
  <span class="foot-nav" style="left:261px">HOME</span>
  <span class="foot-nav" style="left:385px">ABOUT US</span>
  <span class="foot-nav" style="left:525px">PRODUCTS</span>
  <span class="foot-nav" style="left:665px">SERVICES</span>
  <span class="foot-nav" style="left:783px">SHOP</span>
  <span class="foot-nav" style="left:902px">CONTACT</span>
  <p class="copy">© Copyright&nbsp; 2020&nbsp; |&nbsp; All Rights Reserved</p>
  <span class="social" style="left:530px" aria-label="Social link"></span>
  <span class="social" style="left:573px" aria-label="Social link"></span>
  <span class="social" style="left:616px" aria-label="Social link"></span>
</footer>

</body>
</html>
```